basic information

ABN: 62 318 740 256
Electrical lic: 3817452
Work Number; 0471582936

Business name: Dalby's Electrical

Business Colours; White / Dark and light Blue.

logo; is a lighing bolt where the ( ' ) is in Dalby's Electrical.

slogan; "Our prices won't shock you"

Open Hours; 24/7 on call service

Rates;
Mon - Fri, 7am - 4pm = Call out fee $19.95 + $74.95 1st hour, $74.95 an hour after + GST.

Sat - Sun 7am to 4pm = $39.95 callout fee + $109.95 1st hour, 109.95 an hour after + GST.

After hours call out 7 days , 4pm - 7am = $74.95 call out fee + $109.95 minimun 2 hours.

6 points;
1. same day service.
2. local reliable service.
3. All work guaranted.
4 Fully licensed and insured.
5 10 years experience.
6. Free Quotes

Brief decription of my Electrical Business;
I specialize in the following, lighting and power, data & phones, Data racks, Switchboards installation and upgrades, air-conditioning installations & Mantenance, under floor heating, test & tagging, domestic & commercial switchboard inspections, residential rewiring & renovations, motors and controls, LED lighting solutions, Smart metering for domestic and Commercial, energy saving solutions, hot water systems, Art lighting.

Target Market(s)

i am looking for clients in domestic / residential and commercial work places, real state agencies, builders, mantenance contracts on air-conditioning and test & tag contracts and commercial sites for electrical upkeep and breakdown.

Industry/Entity Type

Electrical

```html
<!DOCTYPE html>
<html lang="en">
<head>
<meta charset="utf-8">
<title>Dalby's Electrical – Flyer</title>
<link rel="stylesheet" href="https://fonts.googleapis.com/css2?family=Arimo:wght@400;700&display=swap">
<style>
  :root{
    --bg:#e6e2dc;
    --white:#ffffff;
    --band:#58595b;
    --blue-light:#1e9be0;
    --blue-dark:#0a68b4;
    --accent:#2aa8e8;
    --ink:#4a4a4c;
    --ink-soft:#6b6b6d;
  }
  *{box-sizing:border-box;margin:0;padding:0}
  html,body{width:1200px;height:560px;overflow:hidden;background:var(--bg);font-family:"Arimo",Arial,sans-serif}
  .canvas{position:relative;width:1200px;height:560px}

  .card{position:absolute;top:60px;height:436px;background:var(--white);overflow:hidden;box-shadow:0 2px 6px rgba(0,0,0,.18)}
  .card--front{left:20px;width:564px}
  .card--back{left:616px;width:566px}

  .band{position:absolute;left:0;right:0;height:10px;background:var(--band)}
  .panel{position:absolute;left:0;right:0;background:linear-gradient(135deg,var(--blue-light) 0%,var(--blue-dark) 100%)}

  .brand{position:absolute;font-weight:700;text-transform:uppercase;line-height:1;color:var(--ink);letter-spacing:.5px;white-space:nowrap}
  .brand__name{display:block;font-size:13px}
  .brand--light{color:var(--white)}

  .phone{position:absolute;display:flex;align-items:center;gap:6px;font-weight:700;color:var(--ink);white-space:nowrap}
  .phone svg{fill:var(--accent)}
  .oncall{position:absolute;font-size:18px;color:var(--ink);white-space:nowrap}
  .oncall b{color:var(--accent);font-weight:700}

  /* front */
  .rates{position:absolute;left:14px;top:14px;width:160px;height:271px;overflow:hidden;background:var(--white);padding:12px 10px;box-shadow:0 2px 4px rgba(0,0,0,.25)}
  .rates__title{font-size:19px;font-weight:700;color:var(--accent);margin-bottom:12px}
  .rates__period{font-size:12.5px;line-height:16px;color:var(--ink);margin-bottom:4px}
  .rates__price{font-size:10px;line-height:13px;color:var(--accent);margin-bottom:12px}
  .photo{position:absolute;background:linear-gradient(160deg,#7f9ec4,#2c3f6b)}
  .contact{position:absolute;left:240px;color:var(--white);font-size:10px;white-space:nowrap}
  .contact svg{fill:var(--accent);vertical-align:-2px;margin-right:4px}
  .slogan{position:absolute;left:388px;top:188px;width:160px;text-align:center;color:var(--white);font-weight:700;font-size:29px;line-height:33px;text-shadow:0 2px 3px rgba(0,0,0,.35)}
  .legal{position:absolute;left:230px;top:398px;width:140px;font-size:6.5px;line-height:8.5px;color:var(--ink-soft);text-align:center;white-space:nowrap}

  /* back */
  .domains__title{position:absolute;left:14px;color:var(--white);font-size:19px;font-weight:700;white-space:nowrap}
  .domains__list{position:absolute;list-style:none;color:var(--white);font-size:9.5px;line-height:12.5px}
  .domains__list li{position:relative;padding-left:8px;margin-bottom:7px}
  .domains__list li::before{content:"";position:absolute;left:0;top:4px;width:3px;height:5px;background:var(--white)}
  .offer{position:absolute;left:390px;width:160px;height:190px;background:var(--white);padding:8px 10px;box-shadow:0 2px 4px rgba(0,0,0,.25)}
  .offer__title{font-size:19px;font-weight:700;color:var(--accent);margin-bottom:8px}
  .offer__list{list-style:none;font-size:11.5px;color:var(--ink);line-height:14px}
  .offer__list li{margin-bottom:9px;padding-left:12px;text-indent:-12px}
  .offer__list b{color:var(--accent);font-weight:700;margin-right:3px}
</style>
</head>
<body>
<div class="canvas">

  <section class="card card--front">
    <div class="brand" style="right:28px;top:32px"><span class="brand__name">Dalby's Electrical</span></div>
    <div class="band" style="top:67px"></div>
    <div class="panel" style="top:77px;height:298px">
      <div class="rates">
        <h2 class="rates__title">Rates</h2>
        <p class="rates__period">Mon - Fri, 7am - 4pm</p>
        <p class="rates__price">$19.95 call out fee<br>+ $74.95 1st hour,<br>$74.95 an hour after + GST</p>
        <p class="rates__period">Sat - Sun, 7am to 4pm</p>
        <p class="rates__price">$39.95 call out fee<br>+ $109.95 1st hour,<br>$109.95 an hour after + GST</p>
        <p class="rates__period">After hours call out<br>7 days, 4pm - 7am</p>
        <p class="rates__price">$74.95 call out fee<br>+ $109.95 min. 2 hours + GST</p>
      </div>
      <div class="photo" style="left:376px;top:0;width:188px;height:169px" role="img" aria-label="Photo of a clenched fist holding glowing electricity"></div>
      <div class="brand brand--light" style="left:216px;top:151px"><span class="brand__name">Dalby's Electrical</span></div>
      <p class="contact" style="top:254px;font-size:11px"><svg width="9" height="11" viewBox="0 0 10 12"><path d="M2 0l2 3-1.2 1.5c.6 1.5 1.7 2.8 3.2 3.6L7.5 7 10 9l-1.5 2.5C4 11 0 6 0 1.5z"/></svg>0471 582 936</p>
      <p class="contact" style="top:272px;font-size:8.5px"><svg width="8" height="8" viewBox="0 0 8 8"><rect width="8" height="8" rx="1"/></svg>Marcus@dalbyselectrical.com.au</p>
      <p class="slogan">Our prices won’t shock you!</p>
    </div>
    <div class="band" style="top:375px"></div>
    <p class="oncall" style="left:14px;top:406px"><b>24/7</b> on call service</p>
    <p class="legal">ABN: 62 318 740 256<br>Electrical license: 3817452<br>Work Number: 0471582936</p>
    <p class="phone" style="left:392px;top:402px;font-size:22px"><svg width="13" height="17" viewBox="0 0 10 12"><path d="M2 0l2 3-1.2 1.5c.6 1.5 1.7 2.8 3.2 3.6L7.5 7 10 9l-1.5 2.5C4 11 0 6 0 1.5z"/></svg>0471 582 936</p>
  </section>

  <section class="card card--back">
    <div class="brand" style="left:28px;top:32px"><span class="brand__name">Dalby's Electrical</span></div>
    <p class="oncall" style="left:202px;top:28px"><b>24/7</b> on call service</p>
    <p class="phone" style="left:392px;top:25px;font-size:22px"><svg width="13" height="17" viewBox="0 0 10 12"><path d="M2 0l2 3-1.2 1.5c.6 1.5 1.7 2.8 3.2 3.6L7.5 7 10 9l-1.5 2.5C4 11 0 6 0 1.5z"/></svg>0471 582 936</p>
    <div class="band" style="top:67px"></div>
    <div class="panel" style="top:77px;height:215px">
      <h2 class="domains__title" style="top:11px">Our main speciality domains are:</h2>
      <ul class="domains__list" style="left:14px;top:42px;width:190px">
        <li>Lighting and power</li>
        <li>Data &amp; phones</li>
        <li>Data racks</li>
        <li>Switchboards installation<br>and upgrades</li>
        <li>Air-conditioning installations<br>and maintenance</li>
        <li>Under floor heating</li>
        <li>Domestic &amp; commercial<br>switchboard inspections</li>
      </ul>
      <ul class="domains__list" style="left:202px;top:42px;width:180px">
        <li>Test &amp; tagging</li>
        <li>Residential rewiring &amp; renovations</li>
        <li>Motors and controls</li>
        <li>LED lighting solutions</li>
        <li>Smart metering for domestic<br>and commercial</li>
        <li>Energy saving solutions</li>
        <li>Hot water systems</li>
        <li>Art lighting</li>
      </ul>
      <div class="offer" style="top:13px">
        <h2 class="offer__title">We offer you:</h2>
        <ol class="offer__list">
          <li><b>1</b>Same day service</li>
          <li><b>2</b>Local reliable service</li>
          <li><b>3</b>All work guaranted</li>
          <li><b>4</b>Fully licensed and insured personnel</li>
          <li><b>5</b>10 years experience</li>
          <li><b>6</b>Free Quotes</li>
        </ol>
      </div>
    </div>
    <div class="band" style="top:292px"></div>
    <div class="photo" style="left:0;top:302px;width:172px;height:134px;background:linear-gradient(160deg,#c9cfd6,#3f4f68)" role="img" aria-label="Photo of an electrician in a hard hat reading plans at a switchboard"></div>
    <div class="photo" style="left:174px;top:302px;width:214px;height:134px;background:linear-gradient(180deg,#e8ecef,#a7b2bd 60%,#5a6f8c)" role="img" aria-label="Photo of an empty bright commercial office interior"></div>
    <div class="photo" style="left:390px;top:302px;width:176px;height:134px;background:linear-gradient(160deg,#b9c4cf,#6d7379)" role="img" aria-label="Photo of technicians servicing a rooftop air-conditioning unit"></div>
  </section>

</div>
</body>
</html>
```